Flyer für Kampfsport und Selbstverteidigung
Zielgruppe
Kampfsportschule für Kinder/Jugendliche und Erwachsene
Martial Arts Wenk
Flyerbeispiel finden Sie im Anhang
Aufgabenstellung
Es soll modern gestaltet sein und mit den Farben: Schwarz, Grau, weiß und rot gearbeitet werden.
Im Anhang ist mein alter Flyer. Der soll als Beispiel für Inhalt und Stil sein.

```html
<!DOCTYPE html>
<html lang="de">
<head>
<meta charset="utf-8">
<title>Martial Arts Wenk – Flyer</title>
<link rel="stylesheet" href="https://fonts.googleapis.com/css2?family=Exo+2:ital,wght@0,400;0,600;0,700;0,800;0,900;1,900&family=Saira+Semi+Condensed:wght@500;600&display=swap">
<style>
  :root {
    --red: #e3161d;
    --red-dark: #a30d12;
    --black: #141414;
    --dark: #232323;
    --grey: #8a8a8a;
    --grey-light: #d9d9d9;
    --white: #ffffff;
    --page: #e4e4e4;
  }
  * { box-sizing: border-box; margin: 0; padding: 0; }
  html, body { width: 1200px; height: 824px; overflow: hidden; background: var(--page); }
  body { position: relative; font-family: "Exo 2", sans-serif; color: var(--white); }

  .flyer { position: absolute; top: 56px; width: 519px; height: 698px; overflow: hidden; background: var(--black); }
  .flyer--front { left: 63px; }
  .flyer--plan { left: 618px; }
  .flyer-bg { position: absolute; inset: 0; width: 100%; height: 100%; }

  .brand { position: absolute; display: flex; align-items: center; gap: 8px; transform: translateX(-50%);
    font-weight: 700; font-size: 19px; color: var(--white); white-space: nowrap; }
  .brand-dot { width: 16px; height: 16px; border-radius: 50%; background: var(--red); }
  .flyer--front .brand { left: 252px; top: 86px; }
  .flyer--plan .brand { left: 263px; top: 111px; }

  .title { position: absolute; font-weight: 900; font-style: italic; text-transform: uppercase;
    color: #e9e9e9; text-shadow: 0 2px 3px rgba(0,0,0,.6); line-height: 1; white-space: nowrap; }
  .front-title { left: 0; width: 519px; text-align: center; }
  .front-title--a { top: 160px; font-size: 54px; }
  .front-title--b { top: 204px; font-size: 66px; }
  .front-sub { position: absolute; left: 100px; width: 300px; text-align: center; font-weight: 900;
    font-size: 20px; line-height: 22px; top: 279px; text-transform: uppercase; white-space: nowrap;
    font-style: italic; letter-spacing: .5px; text-shadow: 0 2px 3px rgba(0,0,0,.6); }

  .disciplines-band { position: absolute; left: 0; top: 347px; width: 519px; height: 168px;
    background: linear-gradient(90deg, #f2f2f2 0%, #dcdcdc 55%, #a9a9a9 100%); border-top: 2px solid var(--red); }
  .disciplines { position: absolute; left: 25px; top: 362px; color: var(--dark); }
  .disciplines h2 { font-weight: 900; font-size: 32px; color: var(--red); line-height: 1; margin-bottom: 5px; }
  .disciplines li { list-style: none; font-weight: 700; font-size: 21px; line-height: 27px; white-space: nowrap; }
  .disciplines li::before { content: "▪ "; }

  .photo { position: absolute; }
  .photo--front { left: 404px; top: 296px; width: 115px; height: 293px;
    background: linear-gradient(160deg, #d8a88c 0%, #7a4a44 35%, #c2307c 60%, #202020 100%); }
  .photo--plan { left: 52px; top: 80px; width: 118px; height: 286px;
    background: linear-gradient(180deg, #c99a7c 0%, #f2f2f2 25%, #e9e9e9 55%, #e3c52a 70%, #f0f0f0 100%); }

  .triangle { position: absolute; left: 57px; top: 550px; width: 0; height: 0;
    border-left: 25px solid transparent; border-right: 25px solid transparent; border-top: 33px solid var(--red); }

  .footer { position: absolute; left: 0; top: 592px; width: 519px; height: 106px;
    background: linear-gradient(180deg, #2a2a2a, #161616); border-top: 3px solid var(--red); text-align: center; }
  .footer-lead { margin-top: 5px; font-size: 17px; color: #bdbdbd; letter-spacing: .5px; }
  .footer-lead b { color: var(--white); font-weight: 800; }
  .footer-address { font-size: 13px; letter-spacing: .8px; margin-top: 1px; }

  .info-rule { position: absolute; left: 24px; right: 24px; display: flex; align-items: center; gap: 10px;
    font-size: 16px; letter-spacing: .5px; text-transform: uppercase; white-space: nowrap; }
  .info-rule::before, .info-rule::after { content: ""; flex: 1; height: 1px; background: #bdbdbd; }
  .contacts { position: absolute; left: 24px; right: 24px; display: flex; justify-content: space-between;
    font-size: 19px; letter-spacing: .6px; white-space: nowrap; }
  .contact { display: flex; align-items: center; gap: 6px; }
  .contact svg { width: 17px; height: 17px; }
  .flyer--front .info-rule { top: 644px; }
  .flyer--front .contacts { top: 664px; }
  .flyer--plan .info-rule { top: 641px; }
  .flyer--plan .contacts { top: 661px; }

  .plan-title { right: 22px; text-align: center; width: 360px; font-size: 38px; }
  .plan-title--a { top: 255px; }
  .plan-title--b { top: 290px; }
  .plan-title--c { top: 320px; font-size: 42px; width: 380px; right: 12px; }

  .schedule { position: absolute; left: 33px; top: 370px; width: 467px; height: 259px;
    display: grid; grid-template-columns: 52px repeat(5, 1fr); grid-template-rows: 44px repeat(5, 1fr);
    gap: 2px; background: var(--white); border: 2px solid var(--white);
    font-family: "Saira Semi Condensed", sans-serif; font-weight: 500; }
  .cell { display: flex; flex-direction: column; justify-content: center; align-items: center;
    font-size: 14px; line-height: 15px; text-align: center; background: var(--dark); }
  .cell--head { font-family: "Exo 2", sans-serif; font-weight: 800; font-size: 18px; background: var(--dark); }
  .cell--time { background: var(--red); font-size: 14px; }
  .cell--red { background: var(--red); }
  .cell--grey { background: #9b9b9b; }
  .cell--pale { background: #cfcfcf; color: #f5f5f5; }
  .cell--blank { background: #e2e2e2; }
  .cell--small { font-size: 12.5px; line-height: 13px; }
  .clock { width: 26px; height: 26px; }
  .cell--corner { background: var(--red-dark); }
</style>
</head>
<body>

<!-- Front -->
<section class="flyer flyer--front">
  <svg class="flyer-bg" viewBox="0 0 519 698" preserveAspectRatio="none" aria-hidden="true">
    <defs>
      <linearGradient id="frontDark" x1="0" y1="0" x2="0" y2="1">
        <stop offset="0" stop-color="#3a3a3a"/><stop offset=".45" stop-color="#1a1a1a"/><stop offset="1" stop-color="#0d0d0d"/>
      </linearGradient>
    </defs>
    <rect width="519" height="698" fill="url(#frontDark)"/>
    <polygon points="0,0 120,0 0,120" fill="#f2f2f2"/>
    <polygon points="20,0 190,0 90,110 150,230 60,340 0,340 0,90" fill="#b3121a"/>
    <polygon points="330,0 500,0 420,110 480,230 390,340 320,340 370,230 300,110" fill="#b3121a"/>
    <polygon points="430,0 519,0 519,170 470,110" fill="#f2f2f2"/>
    <polygon points="150,150 370,150 330,240 190,240" fill="#7c0c10" opacity=".7"/>
    <polygon points="0,310 90,250 180,340 0,340" fill="#5a0b0e" opacity=".8"/>
    <polygon points="450,380 519,300 519,520 470,520" fill="#c8141b"/>
  </svg>

  <div class="brand"><span class="brand-dot"></span>Martial Arts Wenk</div>

  <h1 class="title front-title front-title--a">Martial Arts</h1>
  <div class="title front-title front-title--b">Wenk</div>
  <p class="front-sub">Kampfsport<br>&amp; Selbstverteidigung</p>

  <div class="disciplines-band"></div>
  <div class="photo photo--front" role="img" aria-label="Foto: Mädchen mit pinken Boxhandschuhen im schwarzen Vereinsshirt"></div>
  <div class="disciplines">
    <h2>DISZIPLINEN:</h2>
    <ul>
      <li>Kick-Boxen/Sportkarate</li>
      <li>Jiu-Jitsu Selbstverteidigung</li>
      <li>Tricking</li>
      <li>Ü25 Kick-Boxen</li>
    </ul>
  </div>

  <div class="triangle"></div>

  <footer class="footer">
    <p class="footer-lead">Leitung: <b>Jonas Wenk</b></p>
    <p class="footer-address">Am Sportpark 7b &nbsp;|&nbsp; 26409 Musterfeld</p>
  </footer>
  <div class="info-rule">Info &amp; Probetraining:</div>
  <div class="contacts">
    <span class="contact"><svg viewBox="0 0 24 24"><circle cx="12" cy="12" r="10" fill="none" stroke="#e3161d" stroke-width="2"/><path d="M8 7l2 0 1 3-1.5 1a7 7 0 0 0 3.5 3.5l1-1.5 3 1v2a1.5 1.5 0 0 1-1.5 1.5A9 9 0 0 1 7 8.5 1.5 1.5 0 0 1 8 7z" fill="#e3161d"/></svg>0152 / 3021 7749</span>
    <span class="contact"><svg viewBox="0 0 24 24"><rect x="2" y="5" width="20" height="14" fill="none" stroke="#e3161d" stroke-width="2"/><path d="M2 5l10 8 10-8" fill="none" stroke="#e3161d" stroke-width="2"/></svg>info@martial-arts-wenk.de</span>
  </div>
</section>

<!-- Training plan -->
<section class="flyer flyer--plan">
  <svg class="flyer-bg" viewBox="0 0 519 698" preserveAspectRatio="none" aria-hidden="true">
    <defs>
      <linearGradient id="planDark" x1="0" y1="0" x2="0" y2="1">
        <stop offset="0" stop-color="#2b2b2b"/><stop offset="1" stop-color="#0f0f0f"/>
      </linearGradient>
    </defs>
    <rect width="519" height="698" fill="url(#planDark)"/>
    <polygon points="0,0 60,0 0,60" fill="#f2f2f2"/>
    <polygon points="0,0 190,0 110,120 180,230 60,360 0,360" fill="#b3121a"/>
    <polygon points="330,0 519,0 519,40 460,120 519,200 519,260 420,120" fill="#d3151c"/>
    <polygon points="420,0 519,0 519,60" fill="#f2f2f2"/>
    <polygon points="330,190 440,190 519,300 519,360 460,360" fill="#c8141b"/>
    <polygon points="190,150 330,150 300,230 220,230" fill="#7c0c10" opacity=".6"/>
    <polygon points="430,698 519,620 519,698" fill="#c8141b"/>
  </svg>

  <div class="photo photo--plan" role="img" aria-label="Foto: Mädchen im weißen Kampfanzug mit gelbem Gürtel"></div>
  <div class="brand"><span class="brand-dot"></span>Martial Arts Wenk</div>

  <h1 class="title plan-title plan-title--a">Martial Arts</h1>
  <div class="title plan-title plan-title--b">Wenk</div>
  <div class="title plan-title plan-title--c">Trainingsplan</div>

  <div class="schedule">
    <div class="cell cell--corner"><svg class="clock" viewBox="0 0 24 24"><circle cx="12" cy="13" r="9" fill="none" stroke="#fff" stroke-width="2"/><path d="M12 8v5l3 2M9 2h6" fill="none" stroke="#fff" stroke-width="2"/></svg></div>
    <div class="cell cell--head">MON</div>
    <div class="cell cell--head">DIE</div>
    <div class="cell cell--head">MITT</div>
    <div class="cell cell--head">DONN</div>
    <div class="cell cell--head">FREI</div>

    <div class="cell cell--time">15:00<br>15:50</div>
    <div class="cell">Kick-Boxen<br>3-5 Jahre</div>
    <div class="cell cell--red">Jiu-Jitsu<br>3-6 Jahre</div>
    <div class="cell">Kick-Boxen<br>3-5 Jahre</div>
    <div class="cell cell--red">Jiu-Jitsu<br>3-6 Jahre</div>
    <div class="cell">Kick-Boxen<br>3-5 Jahre</div>

    <div class="cell cell--time">16:00<br>16:50</div>
    <div class="cell">Kick-Boxen<br>6-7 Jahre</div>
    <div class="cell cell--red">Jiu-Jitsu<br>7-12 Jahre</div>
    <div class="cell">Kick-Boxen<br>6-7 Jahre</div>
    <div class="cell cell--red">Jiu-Jitsu<br>7-12 Jahre</div>
    <div class="cell cell--small">Kick-Boxen<br>ab 7 Jahre<br>Ab Gelbgurt</div>

    <div class="cell cell--time">17:00<br>18:50</div>
    <div class="cell">Kick-Boxen<br>8-10 Jahre</div>
    <div class="cell cell--grey">Tricking<br>ab 6 Jahre</div>
    <div class="cell">Kick-Boxen<br>8-10 Jahre</div>
    <div class="cell cell--grey">Tricking<br>ab 6 Jahre</div>
    <div class="cell cell--blank"></div>

    <div class="cell cell--time">18:15<br>19:15</div>
    <div class="cell">Kick-Boxen<br>10-12 Jahre</div>
    <div class="cell cell--pale">Kick-Boxen<br>Ü25 Gruppe</div>
    <div class="cell">Kick-Boxen<br>10-12 Jahre</div>
    <div class="cell cell--pale">Kick-Boxen<br>Ü25 Gruppe</div>
    <div class="cell cell--blank"></div>

    <div class="cell cell--time">19:30<br>21:00</div>
    <div class="cell">Kick-Boxen<br>ab 13 Jahre</div>
    <div class="cell cell--blank"></div>
    <div class="cell">Kick-Boxen<br>ab 13 Jahre</div>
    <div class="cell cell--blank"></div>
    <div class="cell cell--blank"></div>
  </div>

  <div class="info-rule">Info &amp; Probetraining:</div>
  <div class="contacts">
    <span class="contact"><svg viewBox="0 0 24 24"><circle cx="12" cy="12" r="10" fill="none" stroke="#e3161d" stroke-width="2"/><path d="M8 7l2 0 1 3-1.5 1a7 7 0 0 0 3.5 3.5l1-1.5 3 1v2a1.5 1.5 0 0 1-1.5 1.5A9 9 0 0 1 7 8.5 1.5 1.5 0 0 1 8 7z" fill="#e3161d"/></svg>0152 / 3021 7749</span>
    <span class="contact"><svg viewBox="0 0 24 24"><rect x="2" y="5" width="20" height="14" fill="none" stroke="#e3161d" stroke-width="2"/><path d="M2 5l10 8 10-8" fill="none" stroke="#e3161d" stroke-width="2"/></svg>info@martial-arts-wenk.de</span>
  </div>
</section>

</body>
</html>
```